KTR Business Cards

We require business cards for our business. We would like a matte black back to the card, with our logo centred in the middle. The front side of the card is open to design.

Target Market(s)

Clients looking for legal services (professional)

Industry/Entity Type

Legal

Contact Information for Business Card

Dario Velkenor
Partner
Mobile: 0471 386 524
Email: dario@ktrlaw.co
Website: www.ktrlaw.co
Level 3, 118 Pembury Street
Sydney NSW 2000

Font styles to use
Other font styles liked:
• Avenir

Colors
f04a50
ffffff
1b1b1b

Requirements
Must have
• Black back with logo included in the centre of the card.
• Our font is Avenir.

```html
<!DOCTYPE html>
<html lang="en">
<head>
<meta charset="utf-8">
<title>KTR Legal – Business Cards</title>
<link href="https://fonts.googleapis.com/css2?family=Nunito+Sans:wght@400;600;700&display=swap" rel="stylesheet">
<style>
  :root {
    --red: #f04a50;
    --deep-red: #d3234a;
    --white: #ffffff;
    --ink: #1b1b1b;
    --backdrop: #3a302c;
    --matte: #1f1f1f;
  }
  * { margin: 0; padding: 0; box-sizing: border-box; }
  html, body { width: 1200px; height: 715px; overflow: hidden; }
  body {
    background: var(--backdrop);
    font-family: "Nunito Sans", sans-serif;
    position: relative;
  }
  .card {
    position: absolute;
    top: 209px;
    width: 520px;
    height: 297px;
    border-radius: 4px;
    overflow: hidden;
    box-shadow: 0 10px 26px rgba(0,0,0,.45);
  }
  /* Back */
  .card-back {
    left: 50px;
    background: var(--matte);
    border-bottom: 5px solid var(--deep-red);
    display: flex;
    align-items: center;
    justify-content: center;
  }
  .back-brand {
    display: flex;
    align-items: center;
    gap: 14px;
    color: var(--white);
    font-weight: 700;
    font-size: 34px;
    letter-spacing: 3px;
  }
  .back-brand .mark { width: 22px; height: 22px; background: var(--deep-red); }

  /* Front */
  .card-front { left: 630px; background: var(--white); color: var(--ink); }
  .front-brand {
    position: absolute; left: 34px; top: 34px;
    display: flex; align-items: center; gap: 12px;
    font-weight: 700; font-size: 22px; letter-spacing: 1.5px; color: var(--ink);
  }
  .front-brand .mark { width: 16px; height: 16px; background: var(--deep-red); }
  .divider {
    position: absolute; left: 34px; right: 34px; top: 146px;
    height: 1px; background: var(--deep-red);
  }
  .holder {
    position: absolute; right: 34px; top: 100px; text-align: right;
  }
  .holder-name {
    color: var(--deep-red); font-weight: 600; font-size: 19px;
    letter-spacing: .5px; text-transform: uppercase; line-height: 1.1;
  }
  .holder-role { font-size: 13px; margin-top: 2px; }
  .addresses {
    position: absolute; right: 34px; top: 158px; text-align: right;
    font-size: 13px; line-height: 1.45;
  }
  .contacts {
    position: absolute; left: 34px; top: 158px;
    list-style: none; font-size: 12.5px; line-height: 1.45;
  }
  .contacts li { display: flex; align-items: center; gap: 7px; }
  .contacts svg { width: 9px; height: 9px; fill: none; stroke: var(--deep-red); stroke-width: 1.4; }
  .swoosh { position: absolute; left: 0; bottom: 0; width: 520px; height: 60px; }
</style>
</head>
<body>
  <section class="card card-back" aria-label="Card back">
    <div class="back-brand"><span class="mark"></span>KTR LEGAL</div>
  </section>

  <section class="card card-front" aria-label="Card front">
    <div class="front-brand"><span class="mark"></span>KTR LEGAL</div>

    <div class="holder">
      <p class="holder-name">Dario Velkenor</p>
      <p class="holder-role">Partner</p>
    </div>
    <div class="divider"></div>

    <ul class="contacts">
      <li><svg viewBox="0 0 10 10"><path d="M2 1 L4 1 L4.5 3 L3.3 4 Q4.5 6 6 6.7 L7 5.5 L9 6 L9 8 Q5 9 1 1.5Z"/></svg>(07) 3924 7106</li>
      <li><svg viewBox="0 0 10 10"><rect x="2.5" y="0.8" width="5" height="8.4" rx="1"/></svg>0471 386 524</li>
      <li><svg viewBox="0 0 10 10"><rect x="0.8" y="2" width="8.4" height="6"/><path d="M0.8 2 L5 5.5 L9.2 2"/></svg>dario@ktrlaw.co</li>
      <li><svg viewBox="0 0 10 10"><circle cx="5" cy="5" r="4"/><path d="M1 5 H9 M5 1 Q2.5 5 5 9 Q7.5 5 5 1"/></svg>www.ktrlaw.co</li>
    </ul>

    <address class="addresses" style="font-style:normal">
      Level 11, 7 Marlin Court<br>
      Carrara QLD 4211<br>
      Level 3, 118 Pembury Street<br>
      Sydney NSW 2000
    </address>

    <svg class="swoosh" viewBox="0 0 520 60" preserveAspectRatio="none" aria-hidden="true">
      <path d="M0 6 L230 34 Q250 37 270 38 L520 38 L520 60 L0 60Z" fill="var(--red)"/>
      <path d="M0 12 L230 38 Q250 41 270 42 L520 42 L520 60 L0 60Z" fill="var(--deep-red)" opacity=".55"/>
      <path d="M0 1 L232 30" stroke="var(--ink)" stroke-width="2.5" fill="none"/>
    </svg>
  </section>
</body>
</html>
```